Promotional business a5 Notepad design

I am looking for a custom a5 notepad design as a promotional item to give away to customers etc.
Attached will be a desk planner we had designed feel free to use as a reference.
We want the notepad to have lines running horizontal not squares like the desk planner example.

Industry/Entity Type

Hydraulic / industrial

Colors

Designer to choose colors to be used in the design.

```html
<!DOCTYPE html>
<html lang="en">
<head>
<meta charset="utf-8">
<title>Meridian Hose &amp; Couplings – A5 Notepad</title>
<link href="https://fonts.googleapis.com/css2?family=Arimo:wght@400;700&display=swap" rel="stylesheet">
<style>
  :root {
    --backdrop: #a2a2a4;
    --paper: #ffffff;
    --ink: #1a1a1a;
    --brand-blue: #1230b8;
    --rule: #6e6e6e;
    --band-dark: #141414;
  }
  html, body {
    margin: 0;
    width: 1200px;
    height: 900px;
    overflow: hidden;
    background: var(--backdrop);
    font-family: "Arimo", Arial, sans-serif;
  }
  .notepad {
    position: absolute;
    left: 325px;
    top: 60px;
    width: 550px;
    height: 780px;
    background: var(--paper);
  }
  .brand {
    position: absolute;
    left: 38px;
    top: 37px;
    display: flex;
    align-items: center;
    gap: 8px;
    color: var(--brand-blue);
    font-weight: 700;
    font-size: 14px;
    letter-spacing: 0.3px;
    white-space: nowrap;
  }
  .brand-dot {
    width: 46px;
    height: 46px;
    border-radius: 50%;
    background: var(--brand-blue);
    flex: none;
  }
  .contact {
    position: absolute;
    right: 38px;
    top: 38px;
    margin: 0;
    padding: 0;
    list-style: none;
    font-size: 12.5px;
    color: var(--ink);
    text-align: right;
    line-height: 14.5px;
  }
  .contact li {
    display: flex;
    justify-content: flex-end;
    align-items: center;
    gap: 6px;
  }
  .contact svg { width: 9px; height: 9px; fill: var(--brand-blue); }
  .writing-lines {
    position: absolute;
    left: 38px;
    top: 114.5px;
    width: 474px;
  }
  .writing-lines span {
    display: block;
    height: 29.53px;
    border-bottom: 1px solid var(--rule);
    box-sizing: border-box;
  }
  .dash-band {
    position: absolute;
    left: 0;
    top: 743px;
    width: 550px;
    height: 8px;
    display: flex;
    gap: 3.6px;
    overflow: hidden;
  }
  .dash-band span {
    flex: none;
    width: 39px;
    height: 8px;
    background: var(--band-dark);
  }
  .footer-band {
    position: absolute;
    left: 0;
    bottom: 0;
    width: 550px;
    height: 27px;
    background: var(--brand-blue);
    color: #fff;
    font-size: 11px;
    display: flex;
    align-items: center;
    justify-content: center;
    gap: 4px;
  }
  .footer-band svg { width: 8px; height: 10px; fill: #fff; }
</style>
</head>
<body>
  <main class="notepad">
    <header>
      <div class="brand">
        <span class="brand-dot"></span>
        <span class="brand-name">MERIDIAN HOSE &amp; COUPLINGS</span>
      </div>
      <ul class="contact">
        <li>08 5550 1234
          <svg viewBox="0 0 10 10"><path d="M2 0.5 L4 2.8 L3 4 Q4.2 6 6 7 L7.2 6 L9.5 8 L8.3 9.5 Q3.5 9 0.5 1.7 Z"/></svg>
        </li>
        <li>0400 555 019
          <svg viewBox="0 0 10 10"><path d="M2 0.5 L4 2.8 L3 4 Q4.2 6 6 7 L7.2 6 L9.5 8 L8.3 9.5 Q3.5 9 0.5 1.7 Z"/></svg>
        </li>
        <li>email@meridianhose.com.au
          <svg viewBox="0 0 10 10"><path d="M0 2 H10 V8 H0 Z M0.8 2.6 L5 5.4 L9.2 2.6 V3.4 L5 6.2 L0.8 3.4 Z" fill-rule="evenodd"/></svg>
        </li>
      </ul>
    </header>

    <section class="writing-lines" aria-label="Lined writing area">
      <span></span><span></span><span></span><span></span><span></span>
      <span></span><span></span><span></span><span></span><span></span>
      <span></span><span></span><span></span><span></span><span></span>
      <span></span><span></span><span></span><span></span><span></span>
    </section>

    <div class="dash-band">
      <span></span><span></span><span></span><span></span><span></span>
      <span></span><span></span><span></span><span></span><span></span>
      <span></span><span></span><span></span><span></span>
    </div>

    <footer class="footer-band">
      <svg viewBox="0 0 8 10"><path d="M4 0 A4 4 0 0 1 8 4 C8 6.5 4 10 4 10 C4 10 0 6.5 0 4 A4 4 0 0 1 4 0 Z M4 2.4 A1.6 1.6 0 1 0 4 5.6 A1.6 1.6 0 1 0 4 2.4 Z" fill-rule="evenodd"/></svg>
      <span>Servicing The Northgate Metropolitan Area</span>
    </footer>
  </main>
</body>
</html>
```